Regional and National Rugby Training and Player Development Company

We need a new responsive website design that is easy to navigate and encourages people to register for our programs.

Registration and payment could be written into the site but it can also be externally integrated as it is currently.

I want clean lines, bright images, and a webpage that is easy to update and manage. Currently using WordPress.
Updates

Ferncrest Rugby runs four programs:  Junior Sunfield Rugby Clinics, Frostline Court Tag Rugby, Bloomtide Skills Clinics, and the "Athlete Growth Pathway" otherwise known as the Forge

Ultimately, Ferncrest Rugby wants to attract the top players across the province of Ontario to join our corner-stone program, the Frostline Forge.

We have had many players play at the provincial level and a select handful go on to represent Canada.  We aspire to set the standard for off-season junior rugby player development.

Reason: 1) Laptop crashed on Thurs. which meant I couldn't make a fair decision this weekend. 2). There are FIVE very good designs, each somewhat unique. I want to see what designers come up with when I outline what I like in each as a requirement of what has been provided. Thank you for your understanding and efforts in this regard. Sincerely, MB Sent from my iPad

Thank you for all your efforts and patience in this design campaign, I truly appreciate it.  Apologies for the lack of communication but as a full-time high school teacher, sometimes my "real job" gets put to the side.  

I have reduced over 30 designs to five... you are the five remaining I hope to take certain aspects of each that I like best and provide some feedback to you the designers, in order to make final adjustments before my final decision.

I hope you find this process agreeable and again, thank you for your patience and efforts in this campaign.  I think each of your designs look fantastic and are a drastic and valuable improvement of what I have been using up to this point.

Appreciatively,

MB

Voting poll results are in and there are three distinct leaders... going to focus on these three this week and come to a final decision before Friday.

Each designer will be contacted privately to provide some feedback and see what the best final product can look like.

Thank you for your patience and high-quality work!

MB

Reason: Just too much going on at the moment and trying to stay on top of this. Apologies to all. Just had the results of the voting poll come in and have reduced choices to two clear leaders with a third alternate. Going to provide feedback for all three today and hope to make final decision by Friday. Thank you for your efforts.

Target Market(s)

Junior rugby players (boys and girls) between the ages of 12 and 20... more importantly, their parents!

Requirements
Must have
• Must have high-resolution, clean lines, and encourage registration in programs. I would like it to be integrated with my YouTube page as well as other social media.

```html
<!DOCTYPE html>
<html lang="en">
<head>
<meta charset="utf-8">
<title>Ferncrest Rugby Canada</title>
<link rel="stylesheet" href="https://fonts.googleapis.com/css2?family=Oswald:wght@300;400&family=Pathway+Gothic+One&display=swap">
<style>
:root{
  --red:#d0181f;
  --red-dark:#a80d10;
  --black:#0d0d0d;
  --ink:#3a3a3a;
  --body:#666;
  --grey-band:#4a4a4a;
  --panel:#efefef;
  --rule:#d6d6d6;
  --white:#fff;
}
*{box-sizing:border-box;margin:0;padding:0}
html,body{width:900px;height:1200px;overflow:hidden;background:var(--white)}
body{position:relative;font-family:"Pathway Gothic One",sans-serif;color:var(--body)}
.abs{position:absolute}
.head{font-family:"Oswald",sans-serif;font-weight:300;text-transform:uppercase;color:var(--ink);letter-spacing:.2px}
.head em{font-style:normal;color:var(--red);font-weight:400}

/* header */
.site-header{left:0;top:0;width:900px;height:94px;background:linear-gradient(90deg,#1a1a1a,#2a2a2a 30%,#050505 60%,#000)}
.brand{left:98px;top:22px;display:flex;align-items:center;gap:10px}
.brand-mark{width:40px;height:40px;border-radius:50%;background:var(--red)}
.brand-name{font-family:"Oswald",sans-serif;font-weight:400;font-size:17px;line-height:20px;color:var(--red);text-transform:uppercase;letter-spacing:1px;text-align:center}
.social{left:730px;top:12px;display:flex;gap:5px}
.social span{width:18px;height:18px;background:#5a5a5a;border-radius:3px}
.search{left:707px;top:37px;width:131px;height:19px;background:#3d3d3d;border-radius:2px}
.search svg{position:absolute;right:5px;top:3px}
.nav{left:0;top:60px;width:900px;height:34px}
.nav a{position:absolute;top:2px;font-family:"Oswald",sans-serif;font-size:15px;color:var(--white);text-decoration:none;text-transform:uppercase}
.nav .current::after{content:"";position:absolute;left:-8px;right:-8px;top:27px;height:4px;background:var(--red)}

/* hero */
.hero{left:0;top:94px;width:900px;height:305px;background:linear-gradient(100deg,#3b3a45 0%,#6d6a6c 35%,#b7b3ad 60%,#7d756e 85%,#4a4547 100%)}
.hero-caption{left:98px;top:208px;width:358px;height:143px;background:rgba(35,35,35,.82)}
.hero-caption h1{position:absolute;left:20px;top:12px;font-family:"Oswald",sans-serif;font-weight:400;font-size:35px;line-height:39px;color:var(--white);text-transform:uppercase}
.btn{display:block;background:var(--red);color:var(--white);font-family:"Oswald",sans-serif;text-transform:uppercase;text-align:center;border-radius:2px}
.hero-caption .btn{position:absolute;left:21px;top:102px;width:105px;height:27px;font-size:15px;line-height:27px}
.dots{left:416px;top:374px;display:flex;gap:5px}
.dots span{width:13px;height:13px;border-radius:50%;background:var(--white)}

/* content */
p{font-size:12px;line-height:17.4px}
.welcome h2{left:97px;top:426px;font-size:18px}
.welcome p{left:97px;top:452px;width:468px}
.col h3{font-size:18px;padding-bottom:6px;border-bottom:3px solid var(--rule);width:214px}
.col p{margin-top:10px}
.mission{left:97px;top:520px;width:214px}
.vision{left:349px;top:520px;width:216px}
.divider{left:97px;top:684px;width:466px;height:1px;background:var(--rule)}
.continuum h2{left:97px;top:692px;font-size:18px}
.arrows{left:543px;top:697px}
.video{left:97px;top:725px;width:250px;height:152px;border:2px solid #bbb;background:linear-gradient(#2c3848 0%,#4d5c66 40%,#3f7a32 55%,#2f6626 100%)}
.video .bar{position:absolute;left:0;bottom:0;width:100%;height:10px;background:#111}
.video .progress{position:absolute;left:24px;bottom:4px;width:42px;height:2px;background:var(--red)}
.video .play{position:absolute;left:108px;top:63px;width:34px;height:22px;border-radius:5px;background:var(--red)}
.video .play::after{content:"";position:absolute;left:13px;top:6px;border-left:9px solid var(--white);border-top:5px solid transparent;border-bottom:5px solid transparent}
.grade{left:370px;top:720px}
.grade h4{font-family:"Oswald",sans-serif;font-weight:300;color:var(--red);font-size:15px}
.grade .lead{margin-top:4px;font-size:12px}
.ticks{list-style:none;margin-top:7px}
.ticks li{font-size:12px;line-height:25px;padding-left:15px;position:relative}
.ticks li::before{content:"";position:absolute;left:2px;top:7px;width:4px;height:8px;border:solid var(--red);border-width:0 2px 2px 0;transform:rotate(40deg)}
.continuum-register{left:367px;top:850px;width:105px;height:27px;font-size:15px;line-height:27px}

/* sidebar */
.programs{left:577px;top:430px;width:225px;height:437px;background:var(--panel);border-radius:3px}
.programs h2{position:absolute;left:12px;top:10px;font-size:17px;white-space:nowrap}
.feature{position:absolute;left:13px;top:39px;width:199px;height:253px;background:var(--white);border:1px solid var(--rule)}
.feature h3{height:27px;background:linear-gradient(#555,#222);color:var(--white);font-family:"Oswald",sans-serif;font-weight:300;font-size:12px;line-height:27px;padding-left:10px;text-transform:uppercase}
.feature .photo{position:absolute;left:10px;top:40px;width:178px;height:100px;background:linear-gradient(#8a3b3e,#4b5f3a 55%,#5b8b3a)}
.feature p{position:absolute;left:10px;top:146px;width:180px;font-size:11px;line-height:15.2px}
.feature .more{position:absolute;right:13px;top:225px;font-family:"Oswald",sans-serif;font-weight:300;color:var(--red);font-size:14px;text-transform:uppercase}
.program-list{position:absolute;left:13px;top:301px;width:199px;list-style:none}
.program-list li{height:30px;margin-bottom:1.5px;background:linear-gradient(#fff,#ebebeb);border:1px solid var(--rule);font-family:"Oswald",sans-serif;font-weight:300;font-size:12px;line-height:28px;padding-left:10px;color:#333;text-transform:uppercase}

/* news band */
.band{left:0;top:893px;width:900px;height:223px;background:var(--grey-band)}
.band .head{color:var(--white);font-size:17px}
.news h2{left:97px;top:906px}
.news-item{left:97px;width:440px}
.news-item .thumb{position:absolute;left:0;top:3px;width:71px;height:63px;border:2px solid var(--red);background:linear-gradient(#8f8a80,#4f5a3c)}
.news-item h3{position:absolute;left:85px;top:0;font-family:"Oswald",sans-serif;font-weight:300;color:#e2262b;font-size:15px;text-transform:uppercase}
.news-item p{position:absolute;left:85px;top:22px;width:355px;font-size:11px;line-height:15px;color:#ddd}
.news-rule{left:95px;top:1023px;width:439px;height:1px;background:#666}
.testimonials h2{left:577px;top:906px}
.testi-arrows{left:783px;top:911px}
.quote{left:577px;top:940px;width:225px;height:122px;background:#111;border-radius:2px}
.quote p{position:absolute;left:16px;top:11px;width:203px;font-size:11px;line-height:15.2px;color:#eee;text-indent:26px}
.quote .mark{position:absolute;font-family:"Oswald",sans-serif;font-size:36px;line-height:36px;color:#999}
.quote::after{content:"";position:absolute;left:58px;bottom:-14px;border-top:14px solid #111;border-left:24px solid transparent}
.author{left:577px;top:1080px;font-size:12px;color:var(--white)}

/* footer */
.footer{left:0;top:1116px;width:900px;height:84px;background:var(--red-dark)}
.footer .brand-mark{position:absolute;left:102px;top:18px;width:44px;height:44px;background:#ce2a2a}
.copyright{left:165px;top:1146px;font-size:12px;color:var(--white)}
.copyright span{color:#6d0507}
.footer-nav{left:528px;top:1152px;font-family:"Oswald",sans-serif;font-size:9px;color:var(--white);text-transform:uppercase;word-spacing:1px}
</style>
</head>
<body>

<header class="site-header abs">
  <div class="brand abs">
    <span class="brand-mark"></span>
    <span class="brand-name">Ferncrest Rugby<br>Canada</span>
  </div>
  <div class="social abs" aria-label="Social links"><span></span><span></span><span></span><span></span><span></span></div>
  <div class="search abs">
    <svg width="14" height="13" viewBox="0 0 14 13"><circle cx="5" cy="5" r="3.8" fill="none" stroke="#fff" stroke-width="1.6"/><line x1="8" y1="8" x2="12.5" y2="12" stroke="#fff" stroke-width="2"/></svg>
  </div>
  <nav class="nav abs">
    <a class="current" style="left:423px">Home</a>
    <a style="left:477px">Player Development</a>
    <a style="left:612px">Community</a>
    <a style="left:698px">FRC News</a>
    <a style="left:774px">Contact Us</a>
  </nav>
</header>

<section class="hero abs" role="img" aria-label="Rugby players in white kit running with the ball during a match">
</section>
<div class="hero-caption abs">
  <h1>We make<br>good players great !</h1>
  <a class="btn">Register Now</a>
</div>
<div class="dots abs"><span></span><span></span><span></span><span></span></div>

<section class="welcome">
  <h2 class="head abs">Welcome to <em>Ferncrest Rugby</em></h2>
  <p class="abs">Aliquam molestie, mi et imperdiet euismod, dui purus auctor tellus, et interdum lacus lectus et ante. Sed accumsan sollicitudin sapien, sit amet adipiscing turpis gravida ac. In congue, neque ac lobortis volutpat, libero mauris varius mi, vitae suscipit ipsum ligula vitae risus.</p>
</section>

<div class="col mission abs">
  <h3 class="head">Our <em>Mission</em></h3>
  <p>Ferncrest Rugby Canada is about making skilled, informed, and knowledgeable players. Our mission is to develop young players within an environment that is challenging, yet rewarding in order to see them attain their goals in the sport of rugby.</p>
</div>
<div class="col vision abs">
  <h3 class="head">Our <em>Vision</em></h3>
  <p>We want our players to enjoy their experience and benefit from their efforts. Ferncrest Rugby is determined to contribute to rugby in Canada by working with young aspiring<br>players who are willing to sacrifice their time and energy in pursuit of their goals.</p>
</div>

<div class="divider abs"></div>
<section class="continuum">
  <h2 class="head abs">Learning <em>Continum</em></h2>
  <svg class="arrows abs" width="20" height="12" viewBox="0 0 20 12"><path d="M6 1 1 6l5 5M14 1l5 5-5 5" fill="none" stroke="#555" stroke-width="1.6"/></svg>
  <div class="video abs" role="img" aria-label="Video of a junior rugby session on an indoor field">
    <span class="play"></span><span class="bar"></span><span class="progress"></span>
  </div>
  <div class="grade abs">
    <h4>U10-12</h4>
    <p class="lead">Emphasis for this age grade:</p>
    <ul class="ticks">
      <li>Fun &amp; Enjoyment</li>
      <li>Skill Introduction</li>
      <li>Modified Games</li>
    </ul>
  </div>
  <a class="btn continuum-register abs">Register Now</a>
</section>

<aside class="programs abs">
  <h2 class="head">Player <em>Development Programs</em></h2>
  <div class="feature">
    <h3>The Junior Academy</h3>
    <div class="photo" role="img" aria-label="Young rugby players lying on the grass with a ball"></div>
    <p>Ferncrest Rugby uses a player-centred model of learning that best provides for developmental needs of young aspiring rugby players. Our programs are designed for players ages, 10 to 18, with the understanding that the players.</p>
    <span class="more">Read More</span>
  </div>
  <ul class="program-list">
    <li>Frostline Forge</li>
    <li>Summer Kids Camps</li>
    <li>Frostline Court Tag Rugby</li>
    <li>Community Initiative</li>
  </ul>
</aside>

<section class="band abs"></section>
<h2 class="head news abs" style="left:97px;top:906px;color:#fff;font-size:17px">Latest News from FRC</h2>
<article class="news-item abs" style="top:944px">
  <div class="thumb" role="img" aria-label="Team photo from summer camp"></div>
  <h3>Summer Camp Club Tour 2013</h3>
  <p>This summer, Ferncrest Rugby will once again bring the latest skills, drills, and games to Ontario's young and aspiring rugby players. We have a talented staff of current and former junior National team players...</p>
</article>
<div class="news-rule abs"></div>
<article class="news-item abs" style="top:1033px">
  <div class="thumb" role="img" aria-label="Players in a tackle drill on grass"></div>
  <h3>Summer Camp Club Tour 2013</h3>
  <p>This summer, Ferncrest Rugby will once again bring the latest skills, drills, and games to Ontario's young and aspiring rugby players. We have a talented staff of current and former junior National team players...</p>
</article>

<h2 class="head abs" style="left:577px;top:906px;color:#fff;font-size:17px">Testimonials</h2>
<svg class="testi-arrows abs" width="20" height="12" viewBox="0 0 20 12"><path d="M6 1 1 6l5 5M14 1l5 5-5 5" fill="none" stroke="#fff" stroke-width="1.6"/></svg>
<blockquote class="quote abs">
  <span class="mark" style="left:10px;top:4px">&ldquo;</span>
  <p>Personally, I see so much benefit to the program you run: there is a definite need for this level of training in our [rugby] community and others. I can't believe the progress that the athletes made and their overall desire to improve for the love of the game.....</p>
  <span class="mark" style="left:170px;top:88px">&rdquo;</span>
</blockquote>
<p class="author abs">Dale Morrow Assistant Coach</p>

<footer class="footer abs">
  <span class="brand-mark"></span>
</footer>
<p class="copyright abs">Copyright © 2013 <span>Ferncrest Rugby Canada</span>.All Right Reserved</p>
<p class="footer-nav abs">Home &nbsp;/&nbsp; Player Development &nbsp;/&nbsp; Community &nbsp;/&nbsp; FRC News &nbsp;/&nbsp; Contact Us</p>

</body>
</html>
```